Gin Bottle Label - 'Copper Kites Over Marsh'

I would like a label designing for our gin. The name is based on a saying 'Copper kites over marsh' meaning stopping for one last drink before leaving. Id like the label to either show humour or people walking? The wording should be the focus.
Attaches are the company logo and a few ideas for you.

```html
<!DOCTYPE html>
<html lang="en">
<head>
<meta charset="utf-8">
<title>Copper Kites Over Marsh – Gin Label</title>
<link href="https://fonts.googleapis.com/css2?family=Arimo:wght@400&display=swap" rel="stylesheet">
<style>
  :root {
    --canvas: #ffffff;
    --label-top: #f9ab3c;
    --label-mid: #f2a53c;
    --label-bottom: #e09e3c;
    --title: #ffffff;
    --figure-top: #2f5f78;
    --figure-bottom: #b8745a;
  }
  html, body {
    margin: 0;
    padding: 0;
    width: 1200px;
    height: 1200px;
    overflow: hidden;
    background: var(--canvas);
  }
  .canvas {
    position: relative;
    width: 1200px;
    height: 1200px;
  }
  .label {
    position: absolute;
    left: 439px;
    top: 302px;
    width: 320px;
    height: 664px;
    background: linear-gradient(to bottom, var(--label-top) 0%, var(--label-mid) 50%, var(--label-bottom) 100%);
    overflow: hidden;
  }
  .label__title {
    position: absolute;
    left: 51px;
    top: 84px;
    margin: 0;
    font-family: "Arimo", Arial, sans-serif;
    font-weight: 400;
    font-size: 72px;
    line-height: 92px;
    color: var(--title);
    letter-spacing: -0.5px;
    white-space: nowrap;
  }
  .label__title span {
    display: block;
  }
  .label__figure {
    position: absolute;
    left: 206px;
    top: 468px;
    width: 84px;
    height: 172px;
    border-radius: 32px 32px 6px 6px;
    background: linear-gradient(to bottom, var(--figure-top) 0%, var(--figure-top) 62%, var(--figure-bottom) 100%);
    opacity: 0.85;
  }
</style>
</head>
<body>
  <main class="canvas">
    <section class="label">
      <h1 class="label__title">
        <span>Copper</span>
        <span>Kites</span>
        <span>Over</span>
        <span>Marsh</span>
      </h1>
      <div class="label__figure" role="img" aria-label="Cartoon illustration of a cheerful man in a beret and sunglasses raising a cocktail glass"></div>
    </section>
  </main>
</body>
</html>
```